Pet Care Business Card

Dog & Cat Grooming, we come to you or come to Tails and Whiskers Nook
Doggy day care,
Boutique holiday care,
Pet Supplies
All Natural Products used
Have created the logo, which I will forward shortly but need help to have it on flyers business cards ect
email tailsandwhiskersnook@furmail.example
Ph: 0417552630
Colours: Green Black and paws prints nott sure what colour for them
Thank you to all that forwarded their designs, very hard choice and I thank you for your effort, shall recommend this to all my collegues
Thanks Again Jo :)
Business
0417552630
57 upper Kestrel Lane
Brindle QLD 4512

```html
<!DOCTYPE html>
<html lang="en">
<head>
<meta charset="utf-8">
<title>Tails and Whiskers Nook – Business Card</title>
<link rel="stylesheet" href="https://fonts.googleapis.com/css2?family=Exo+2:wght@400;500;700&display=swap">
<style>
  :root {
    --backdrop: #e4e4e4;
    --card: #f7f7f7;
    --green: #2f6a2b;
    --green-light: #93bb72;
    --black-text: #1b1b1b;
    --light-text: #ffffff;
  }
  * { margin: 0; padding: 0; box-sizing: border-box; }
  html, body {
    width: 1200px;
    height: 900px;
    overflow: hidden;
    background: var(--backdrop);
    font-family: "Exo 2", sans-serif;
  }
  .business-card {
    position: absolute;
    left: 100px;
    top: 165px;
    width: 1000px;
    height: 570px;
    background: var(--card);
    overflow: hidden;
    box-shadow: 0 6px 18px rgba(0,0,0,0.12);
  }
  .card-bands {
    position: absolute;
    inset: 0;
    width: 100%;
    height: 100%;
  }
  .band-main { fill: var(--green); }
  .band-swoosh { fill: var(--green-light); }

  .brand {
    position: absolute;
    left: 60px;
    top: 170px;
    display: flex;
    align-items: center;
    gap: 22px;
  }
  .brand-circle {
    width: 118px;
    height: 118px;
    border-radius: 50%;
    border: 5px solid var(--green);
    flex: none;
  }
  .brand-name {
    font-weight: 700;
    font-size: 36px;
    line-height: 1.05;
    color: var(--green);
    width: 270px;
  }

  .person {
    position: absolute;
    left: 480px;
    top: 36px;
  }
  .person-name {
    font-size: 34px;
    font-weight: 500;
    color: var(--green);
    letter-spacing: 1px;
  }
  .person-role {
    font-size: 26px;
    color: var(--black-text);
    letter-spacing: 1px;
  }

  .contact-list {
    position: absolute;
    left: 470px;
    top: 410px;
    list-style: none;
    color: var(--light-text);
    font-size: 24px;
    letter-spacing: 1px;
    line-height: 34px;
  }
  .contact-list li { display: flex; align-items: center; gap: 10px; }
  .contact-icon { width: 20px; height: 20px; flex: none; }
  .contact-icon * { fill: none; stroke: var(--light-text); stroke-width: 2; }

  .location {
    position: absolute;
    left: 660px;
    top: 262px;
    color: var(--light-text);
    font-size: 24px;
    letter-spacing: 1px;
    line-height: 32px;
  }
  .website {
    position: absolute;
    left: 690px;
    top: 360px;
    color: var(--light-text);
    font-size: 24px;
    letter-spacing: 1px;
  }
</style>
</head>
<body>
  <div class="business-card">
    <svg class="card-bands" viewBox="0 0 1000 570" preserveAspectRatio="none" aria-hidden="true">
      <path class="band-swoosh" d="M215 570 C 380 330, 580 190, 790 125 C 600 210, 420 350, 262 570 Z"/>
      <path class="band-main" d="M275 570 C 430 360, 640 200, 1000 78 L 1000 570 Z"/>
    </svg>

    <div class="brand">
      <div class="brand-circle"></div>
      <div class="brand-name">Tails and Whiskers Nook</div>
    </div>

    <div class="person">
      <div class="person-name">Rory Fenwick</div>
      <div class="person-role">president and founder</div>
    </div>

    <ul class="contact-list">
      <li>
        <svg class="contact-icon" viewBox="0 0 20 20"><path d="M5 2 L8 6 L6 8 C7 11 9 13 12 14 L14 12 L18 15 L16 18 C9 18 2 11 2 4 Z"/></svg>
        012 555 0148
      </li>
      <li>
        <svg class="contact-icon" viewBox="0 0 20 20"><rect x="5" y="1" width="10" height="18" rx="2"/><line x1="9" y1="16" x2="11" y2="16"/></svg>
        012 555 0148
      </li>
      <li>
        <svg class="contact-icon" viewBox="0 0 20 20"><rect x="2" y="7" width="16" height="11" rx="1"/><rect x="6" y="2" width="8" height="5"/><line x1="6" y1="12" x2="14" y2="12"/></svg>
        012 555 0148
      </li>
      <li>
        <svg class="contact-icon" viewBox="0 0 20 20"><rect x="2" y="4" width="16" height="12"/><path d="M2 4 L10 11 L18 4"/></svg>
        hello@tailsnook.example
      </li>
    </ul>

    <div class="location">
      14 Copper Mill Court<br>
      Brindle QLD
    </div>
    <div class="website">www.tailsnook.example</div>
  </div>
</body>
</html>
```